High-end Oceanfront Real Estate Group Needs Clean, Modern Web Design

I’m looking for a clean, professional, modern and beautiful homepage web design for a Real Estate group in Southern California, USA.

The group/company is “Marlow on the Shore,” and they specialize in high end (i.e. expensive), oceanfront real estate in the Orange County area.

The look and feel of the page should accentuate the brand qualities: luxurious/expensive, professional, and beautiful (Orange County is one of the most beautiful areas in all the US and we would love the site to emphasize the beautiful beaches and scenery it has to offer).

Looks we like:
• www.brantleyhomesrealty.example
• www.keptbyfenwick.example -- I think the design is pretty out-dated in this site, but I like the organization/layout of the site

Header Tags (I don’t know if we can fit all of these, may need a side-menu, but I’d prefer header title only if possible):
• Welcome
• Featured Listings
• Previously Sold
• Sell
• Property Search
• Team
• Videos
• Blog
• Explore O.C.
• Contact

I have attached the beach and logo pics that we would like to use as the header, a few pictures of the team, and one sample home/view pic which can be used in any of the other sections (for pictures of the homes, just find expensive oceanfront houses and that will be fine).

I promise to provide feedback to each and every design submission. I appreciate the hard work that all of you are putting into your designs. There can be only one contest winner, but I hope to give all of you helpful feedback to submit the best designs possible!

Target Market(s)

Very wealthy home owners of oceanfront properties. These properties are worth several millions of dollars, and thus the site and brand needs to be targeted to very wealthy, successful individuals and families (both US and international buyers).

Industry/Entity Type

Real Estate

Number of Pages Required

2 page

Requirements
Must have
• I don’t want to give too many requirements, because I want to let you all be creative. However, here are the few Must Haves:
• Must submit 2 page designs (a home page and a sub page)
• Must use logo provided
• Focus is mostly on homes, but I would like to include some beach/ocean imagery as well
• The first “item” on the home page should be an accordion/slider which shows pictures of homes and with 1 line of text: “List with the Leader” and two link buttons: “Sell Your Home” and “Buy Your Home”
• Color palette needs to be mainly blues--to match ocean and sky blue
• Exported in all major formats (psd,ai,eps,png,jpeg,etc)
Nice to have
• We don’t necessarily need all of these, but would like to feature most:
• List of videos
• “Meet the Team”—brief team bios and pics
• Link(s) to Blog
• “List with the Leader” – section on why they should choose this firm
• Featured Listings
• Previously Sold

```html
<!DOCTYPE html>
<html lang="en">
<head>
<meta charset="utf-8">
<title>Marlow on the Shore — Oceanfront Real Estate</title>
<link href="https://fonts.googleapis.com/css2?family=Raleway:wght@400;500;600;700;800&family=Open+Sans:ital,wght@0,400;0,600;0,700;1,400&display=swap" rel="stylesheet">
<style>
:root{
  --brand:#1e6fab;
  --sky:#2b8ccc;
  --tag:#3cb5e5;
  --green:#1fa68b;
  --ink:#2a2a2a;
  --muted:#777;
  --line:#e2e2e2;
  --panel:#f0f0f0;
  --footer:#3b3b3b;
  --footer-deep:#333;
  --white:#fff;
}
*{box-sizing:border-box;margin:0;padding:0}
html,body{width:1200px;height:3797px;overflow:hidden}
body{font-family:"Open Sans",Arial,sans-serif;color:var(--ink);background:var(--white);position:relative}
.section{position:absolute;left:0;width:1200px}
.section-title{position:absolute;left:0;width:100%;text-align:center;font-family:"Raleway",Arial,sans-serif;font-weight:700;font-size:35px;letter-spacing:.5px;color:#222}

/* Hero */
.hero{top:0;height:608px;overflow:hidden}
.hero-photo{position:absolute;inset:0;background:linear-gradient(180deg,#5d9dd6 0%,#8cc0e8 22%,#b7d9ef 30%,#3b7fb6 34%,#1f5f94 52%,#3f86b6 68%,#a7c9d9 80%,#d9d7cf 100%)}
.topbar{position:absolute;top:0;left:0;width:100%;height:56px;background:rgba(20,30,40,.55)}
.logo{position:absolute;left:109px;top:0;width:157px;height:152px;background:var(--brand);color:var(--white);font-family:"Raleway",sans-serif;font-weight:500;font-size:25px;line-height:1.15;padding:30px 14px 0;text-transform:uppercase;letter-spacing:1px}
.nav{position:absolute;top:18px;left:400px;display:flex}
.nav a{color:var(--white);text-decoration:none;font-size:14px;font-weight:600;padding:4px 13px}
.nav a.active{background:rgba(255,255,255,.18)}
.hero-tagline{position:absolute;top:228px;width:100%;text-align:center;color:var(--white);font-family:"Raleway",sans-serif;font-weight:600;font-size:18px;letter-spacing:3px}
.hero-head{position:absolute;top:266px;width:100%;text-align:center;color:var(--white);font-family:"Raleway",sans-serif;font-weight:500;font-size:34px;letter-spacing:1px}
.hero-sub{position:absolute;top:320px;left:200px;width:800px;text-align:center;color:var(--white);font-family:"Raleway",sans-serif;font-size:16px;line-height:1.6;letter-spacing:.5px}
.slide-arrow{position:absolute;top:308px;width:38px;height:38px;border-radius:50%;background:rgba(30,30,30,.55)}
.slide-arrow svg{display:block;margin:11px auto}
.hero-cta{position:absolute;left:354px;top:535px;width:489px;height:73px;background:var(--white)}
.btn{position:absolute;top:14px;height:69px;width:224px;color:var(--white);font-family:"Raleway",sans-serif;font-weight:700;font-size:19px;display:flex;align-items:center;justify-content:center;letter-spacing:.5px}
.btn-sell{left:18px;background:var(--green);box-shadow:0 4px 0 #178770}
.btn-buy{left:251px;background:var(--sky);box-shadow:0 4px 0 #216fa5}

/* About */
.about{top:608px;height:501px;background:linear-gradient(90deg,#fff 0%,#fafafa 60%,#f5f5f5 100%)}
.about .section-title{top:64px}
.about-lead{position:absolute;left:109px;top:158px;font-family:"Raleway",sans-serif;font-size:35px;font-weight:400;color:#333}
.about-copy{position:absolute;left:109px;top:218px;width:640px;font-size:13px;line-height:1.7;color:#666}
.about-copy p+p{margin-top:4px}
.agent-photo{position:absolute;left:825px;top:88px;width:260px;height:413px;background:linear-gradient(180deg,#ececec 0%,#d9c6b4 40%,#e7d3bf 100%);border-radius:120px 120px 0 0}

/* Listings */
.listings{top:1109px;height:765px;background:var(--panel)}
.listings .section-title{top:52px}
.card{position:absolute;width:481px;height:248px;background:var(--white);border:1px solid var(--line)}
.card h3{position:absolute;left:18px;top:12px;font-size:15px;font-weight:600;color:#333}
.card-photo{position:absolute;left:18px;top:44px;width:213px;height:146px;background:linear-gradient(180deg,#9cc8ea 0%,#c9dcea 35%,#a99c86 60%,#6e9b4c 100%)}
.card-photo .status{position:absolute;right:0;bottom:0;background:#f08a2c;color:#fff;font-size:10px;padding:3px 8px}
.price{position:absolute;left:231px;top:44px;height:32px;width:230px;background:var(--tag);color:#fff;font-size:15px;font-weight:600;padding:0 10px;display:flex;align-items:center;gap:6px}
.price small{font-size:11px;font-weight:600}
.card-text{position:absolute;left:246px;top:88px;width:210px;font-size:12px;line-height:1.6;color:#888}
.card-more{position:absolute;left:246px;top:160px;font-size:12px;color:#444}
.card-meta{position:absolute;left:0;bottom:0;width:100%;height:38px;border-top:1px solid var(--line);display:flex;align-items:center;gap:26px;padding:0 18px;font-size:11px;color:#555}
.card-meta span{display:flex;align-items:center;gap:6px}
.card-meta i{display:inline-block;width:13px;height:11px;background:#666;border-radius:2px}

/* Videos */
.videos{top:1874px;height:392px;background:var(--white)}
.videos .section-title{top:78px}
.thumb{position:absolute;top:159px;width:228px;height:152px;background:linear-gradient(180deg,#8fc3ec 0%,#cfe2ef 35%,#b6a98d 62%,#5d8f3d 100%)}
.thumb svg{position:absolute;left:84px;top:46px}
.v-arrow{position:absolute;top:222px;width:22px;height:38px;background:#eee;display:flex;align-items:center;justify-content:center}
.v-arrow.dark{background:#333}

/* Sold */
.sold{top:2266px;height:552px;background:linear-gradient(180deg,#2c4a60 0%,#3a6685 35%,#4c7893 60%,#3a5e74 100%)}
.sold .section-title{top:76px;color:var(--white)}
.sold-card{position:absolute;top:170px;width:302px;height:316px;background:var(--white);border-radius:4px;overflow:hidden}
.sold-photo{height:192px;background:linear-gradient(180deg,#2b3d62 0%,#5e7aa2 45%,#c79c64 75%,#6d5b45 100%)}
.sold-card h4{position:absolute;left:14px;top:209px;font-family:"Raleway",sans-serif;font-weight:500;font-size:19px;color:#333}
.sold-where{position:absolute;left:14px;top:246px;font-size:13px;color:#444;line-height:1.5}
.sold-where b{display:block;font-weight:400;font-size:18px;color:var(--brand)}
.view-btn{position:absolute;right:18px;top:253px;border:1px solid var(--sky);color:var(--sky);font-size:12px;padding:8px 14px;border-radius:3px}

/* Testimonials */
.testimonials{top:2818px;height:633px;background:var(--white)}
.testimonials .section-title{top:64px}
.quote{position:absolute;top:180px;height:197px;border:1px solid var(--line);padding:40px 40px 0;text-align:center;font-size:15px;line-height:1.75;color:#666}
.quote .mark{position:absolute;left:22px;top:6px;font-family:Georgia,serif;font-size:46px;color:var(--sky);line-height:1}
.avatar{position:absolute;top:344px;width:110px;height:110px;border-radius:50%;background:linear-gradient(160deg,#e9e9e9,#bdbdbd);border:4px solid #fff}
.quote-name{position:absolute;top:476px;width:448px;text-align:center;font-size:14px;color:#555}
.dots{position:absolute;top:549px;left:531px;display:flex;gap:9px}
.dots span{width:19px;height:19px;border-radius:50%;background:#ccc}
.dots span.on{background:var(--sky)}

/* Footer */
.footer{top:3451px;height:346px;background:var(--footer);color:#ddd}
.footer h5{position:absolute;top:64px;font-family:"Raleway",sans-serif;font-weight:500;font-size:25px;color:#eee}
.sitemap{position:absolute;top:110px;font-size:12px;line-height:1.75;color:#ddd;text-transform:uppercase}
.blog-text{position:absolute;left:520px;top:110px;width:250px;font-size:13px;line-height:1.75;color:#ddd}
.blog-text em{display:block;color:#999}
.contact-row{position:absolute;left:878px;display:flex;align-items:center;gap:24px;font-size:14px;color:#ddd}
.footer-band{position:absolute;left:0;bottom:50px;width:100%;height:90px;background:linear-gradient(180deg,rgba(255,255,255,0) 0%,rgba(255,255,255,.07) 100%)}
.footer-bar{position:absolute;left:0;bottom:0;width:100%;height:50px;background:var(--footer-deep);display:flex;align-items:center;justify-content:space-between;padding:0 109px;font-size:12px;color:#888}
</style>
</head>
<body>

<header class="section hero">
  <div class="hero-photo" role="img" aria-label="Oceanfront beach scene with palm trees, surf and blue sky"></div>
  <div class="topbar"></div>
  <div class="logo">Marlow<br>on the<br>Shore</div>
  <nav class="nav">
    <a class="active">HOME</a><a>FEATURED LISTINGS</a><a>SOLD</a><a>SELL</a><a>TEAM</a><a>VIDEOS</a><a>BLOG</a><a>CONTACT</a>
  </nav>
  <p class="hero-tagline">LIST WITH THE LEADER</p>
  <h1 class="hero-head">WE ARE OFFERING THE BEST REAL ESTATE DEALS</h1>
  <p class="hero-sub">WE AT MARLOWONTHESHORE ARE PRIVILEGED TO HELP PEOPLE FROM ALL OVER THE WORLD FIND THEIR DREAM HOMES</p>
  <div class="slide-arrow" style="left:40px"><svg width="14" height="16" viewBox="0 0 14 16"><path d="M10 2 4 8l6 6" stroke="#fff" stroke-width="3" fill="none"/></svg></div>
  <div class="slide-arrow" style="left:1121px"><svg width="14" height="16" viewBox="0 0 14 16"><path d="M4 2l6 6-6 6" stroke="#fff" stroke-width="3" fill="none"/></svg></div>
  <div class="hero-cta">
    <a class="btn btn-sell">SELL YOUR HOME</a>
    <a class="btn btn-buy">BUY YOUR HOME</a>
  </div>
</header>

<section class="section about">
  <h2 class="section-title">ABOUT US</h2>
  <p class="about-lead">Live Walk Dream.....</p>
  <div class="about-copy">
    <p>Lorem ipsum dolor sit amet, consectetur adipiscing elit. Fusce varius erat lacus, in dictum odio pulvinar a. Proin in dui tortor. Nulla iaculis hendrerit augue ac facilisis. Pellentesque volutpat nunc est, eu convallis quam ultrices sed. Praesent ut ligula eleifend, condimentum quam vitae, luctus ante. Suspendisse tellus turpis, sollicitudin in dapibus quis, consequat egestas dui. Donec vel vulputate mauris. Ut feugiat sed dui ac tristique. Fusce tincidunt erat non rutrum euismod.</p>
    <p>Duis efficitur odio eu massa rhoncus ultricies. Nam venenatis est at neque pulvinar, sed iaculis est scelerisque. Integer aliquam pellentesque erat sit amet egestas. Pellentesque non odio felis. Suspendisse fermentum suscipit risus non eleifend. Phasellus varius sapien sed tellus vulputate, vel facilisis lectus imperdiet.</p>
  </div>
  <div class="agent-photo" role="img" aria-label="Portrait of the lead agent"></div>
</section>

<section class="section listings">
  <h2 class="section-title">FEATURED LISTINGS</h2>

  <article class="card" style="left:109px;top:162px">
    <h3>410 - C, Harbor Lane, Dana Point, CA</h3>
    <div class="card-photo" role="img" aria-label="Two-storey family home with lawn"><span class="status">On Sale</span></div>
    <div class="price">$750,000 <small>– Single Family Home</small></div>
    <p class="card-text">Lorem ipsum dolor sit amet, consectetur adipiscing elit. Fusce varius erat lacus, in dictum odio</p>
    <span class="card-more">More Details ▸</span>
    <div class="card-meta"><span><i></i>821 Sq. Feet</span><span><i></i>3 Bed Rooms</span><span><i></i>2 Bathrooms</span><span><i></i>2 Garages</span></div>
  </article>

  <article class="card" style="left:613px;top:162px">
    <h3>2218 Seacliff Dr, Laguna Beach, CA</h3>
    <div class="card-photo" role="img" aria-label="New construction home with garden"><span class="status">On Sale</span></div>
    <div class="price">$11,50,000 <small>– New Construction</small></div>
    <p class="card-text">Lorem ipsum dolor sit amet, consectetur adipiscing elit. Fusce varius erat lacus, in dictum odio</p>
    <span class="card-more">More Details ▸</span>
    <div class="card-meta"><span><i></i>821 Sq. Feet</span><span><i></i>3 Bed Rooms</span><span><i></i>2 Bathrooms</span><span><i></i>1 Garage</span></div>
  </article>

  <article class="card" style="left:109px;top:438px">
    <h3>3071 Tidewater Ave, Newport</h3>
    <div class="card-photo" role="img" aria-label="White colonial house under blue sky"><span class="status">On Sale</span></div>
    <div class="price">$970,000 <small>– New Construction</small></div>
    <p class="card-text">Lorem ipsum dolor sit amet, consectetur adipiscing elit. Fusce varius erat lacus, in dictum odio</p>
    <span class="card-more">More Details ▸</span>
    <div class="card-meta"><span><i></i>821 Sq. Feet</span><span><i></i>3 Bed Rooms</span><span><i></i>2 Bathrooms</span><span><i></i>3 Garages</span></div>
  </article>

  <article class="card" style="left:613px;top:438px">
    <h3>1480 Coral Crest Rd, San Clemente, CA</h3>
    <div class="card-photo" role="img" aria-label="Modern glass house on a lawn"><span class="status">On Sale</span></div>
    <div class="price">$850,000 <small>– Single Family Home</small></div>
    <p class="card-text">Lorem ipsum dolor sit amet, consectetur adipiscing elit. Fusce varius erat lacus, in dictum odio</p>
    <span class="card-more">More Details ▸</span>
    <div class="card-meta"><span><i></i>821 Sq. Feet</span><span><i></i>3 Bed Rooms</span><span><i></i>2 Bathrooms</span><span><i></i>2 Garages</span></div>
  </article>
</section>

<section class="section videos">
  <h2 class="section-title">VIDEOS</h2>
  <div class="v-arrow" style="left:56px"><svg width="8" height="12"><path d="M6 1 1 6l5 5" stroke="#555" stroke-width="2" fill="none"/></svg></div>
  <div class="thumb" style="left:109px" role="img" aria-label="Video tour of a family home"><svg width="60" height="60"><circle cx="30" cy="30" r="27" fill="rgba(255,255,255,.35)" stroke="#fff" stroke-width="3"/><path d="M24 18v24l19-12z" fill="#fff"/></svg></div>
  <div class="thumb" style="left:360px" role="img" aria-label="Video tour of a modern house"><svg width="60" height="60"><circle cx="30" cy="30" r="27" fill="rgba(255,255,255,.35)" stroke="#fff" stroke-width="3"/><path d="M24 18v24l19-12z" fill="#fff"/></svg></div>
  <div class="thumb" style="left:610px" role="img" aria-label="Video tour of a suburban home"><svg width="60" height="60"><circle cx="30" cy="30" r="27" fill="rgba(255,255,255,.35)" stroke="#fff" stroke-width="3"/><path d="M24 18v24l19-12z" fill="#fff"/></svg></div>
  <div class="thumb" style="left:861px" role="img" aria-label="Video tour of a colonial house"><svg width="60" height="60"><circle cx="30" cy="30" r="27" fill="rgba(255,255,255,.35)" stroke="#fff" stroke-width="3"/><path d="M24 18v24l19-12z" fill="#fff"/></svg></div>
  <div class="v-arrow dark" style="left:1123px"><svg width="8" height="12"><path d="M2 1l5 5-5 5" stroke="#fff" stroke-width="2" fill="none"/></svg></div>
</section>

<section class="section sold" role="img" aria-label="Palm-lined beach at dusk behind sold properties">
  <h2 class="section-title">PREVIOUSLY SOLD</h2>
  <article class="sold-card" style="left:114px">
    <div class="sold-photo" role="img" aria-label="Resort tower lit at night"></div>
    <h4>Lorem Ipsum Doler Sit</h4>
    <p class="sold-where">Some Where<b>California</b></p>
    <a class="view-btn">View Listings</a>
  </article>
  <article class="sold-card" style="left:451px">
    <div class="sold-photo" role="img" aria-label="Glass atrium of a shopping centre" style="background:linear-gradient(180deg,#7fa8c9 0%,#d5e4ee 45%,#9bb3a4 75%,#6f7f73 100%)"></div>
    <h4>Lorem Ipsum Doler Sit</h4>
    <p class="sold-where">Some Where<b>California</b></p>
    <a class="view-btn">View Listings</a>
  </article>
  <article class="sold-card" style="left:787px">
    <div class="sold-photo" role="img" aria-label="Multi-level shopping mall interior" style="background:linear-gradient(180deg,#c9d6df 0%,#e9eef1 40%,#b9a590 75%,#8a7a68 100%)"></div>
    <h4>Lorem Ipsum Doler Sit</h4>
    <p class="sold-where">Some Where<b>California</b></p>
    <a class="view-btn">View Listings</a>
  </article>
</section>

<section class="section testimonials">
  <h2 class="section-title">CUSTOMER TESTIMONIALS</h2>
  <blockquote class="quote" style="left:114px;width:443px"><span class="mark">“</span>"I love that they offer the book online feature. It saves me time from my schedule and it is so easy to do! If you are looking for a trusted and thorough cleaner, look no further!"</blockquote>
  <blockquote class="quote" style="left:641px;width:448px"><span class="mark">“</span>"I love that they offer the book online feature. It saves me time from my schedule and it is so easy to do! If you are looking for a trusted and thorough cleaner, look no further!"</blockquote>
  <div class="avatar" style="left:280px" role="img" aria-label="Customer portrait"></div>
  <div class="avatar" style="left:810px" role="img" aria-label="Customer portrait"></div>
  <p class="quote-name" style="left:111px">– Clara, in Irvine -</p>
  <p class="quote-name" style="left:641px">– Clara, in Irvine -</p>
  <div class="dots"><span class="on"></span><span></span><span></span></div>
</section>

<footer class="section footer">
  <div class="footer-band" role="img" aria-label="Faint city skyline backdrop"></div>
  <h5 style="left:109px">Sitemap</h5>
  <div class="sitemap" style="left:109px">Home<br>Featured Listings<br>Sold<br>Sell</div>
  <div class="sitemap" style="left:320px">Team<br>Videos<br>Blog<br>Contact</div>
  <h5 style="left:520px">Blog</h5>
  <p class="blog-text">Lorem Ipsum Dolor Sit amet and typesetting industry and has been ender is been setting and sett,<em>by Owen Pryce</em></p>
  <h5 style="left:872px">Our Contact</h5>
  <div class="contact-row" style="top:116px"><svg width="20" height="20" viewBox="0 0 20 20"><path d="M4 2l4 4-2 3c1 2 3 4 5 5l3-2 4 4-3 3C9 19 1 11 1 5z" fill="#ddd"/></svg>(555) - 014 - 2270</div>
  <div class="contact-row" style="top:152px"><svg width="22" height="16" viewBox="0 0 22 16"><rect x="1" y="1" width="20" height="14" fill="none" stroke="#ddd" stroke-width="2"/><path d="M1 1l10 8 10-8" fill="none" stroke="#ddd" stroke-width="2"/></svg>info@marlowshore.example</div>
  <div class="footer-bar"><span>© 2014. Marlow on the Shore All Rights Reserved.</span><span>Terms &amp; Conditions &nbsp;|&nbsp; Privacy Policy</span></div>
</footer>

</body>
</html>
```